Verlune Magician

I want the business card for my business to give to people who watch that later I will be employed to show magic here is my website http://www.verlunemagicien-exemple.fr/I want the interesting design , i am very opened for formal and informal, I watch a lot of design so don't stick to the common shape and form but i hope it can also be produced the thing to write on will be the same as in picture that i will upload , i also will upload the logo for you that so can be easy to useDenis CostilleMagicianMAGICIAN VERLUNE 17 rue des Tilleuls - 25000 BESANÇON contact@verlunemagicien-exemple.fr tel. 0381 476 093 tel. 0664 219 570

```html
<!DOCTYPE html>
<html lang="fr">
<head>
<meta charset="utf-8">
<title>Verlune Magicien – carte de visite</title>
<link rel="stylesheet" href="https://fonts.googleapis.com/css2?family=Jost:wght@300;400&family=Didact+Gothic&display=swap">
<style>
  :root {
    --backdrop: #cfd0d2;
    --card: #ffffff;
    --ink: #111111;
    --ink-soft: #2a2a2a;
    --red: #e3262b;
    --ghost: #f3f3f3;
  }
  * { margin: 0; padding: 0; box-sizing: border-box; }
  html, body {
    width: 1200px; height: 900px; overflow: hidden;
    background: var(--backdrop);
  }
  .canvas { position: relative; width: 1200px; height: 900px; }

  .card {
    position: absolute; top: 165px;
    width: 341px; height: 599px;
    background: var(--card);
  }
  .card--front { left: 218px; }
  .card--back  { left: 635px; }

  .portrait { position: absolute; }
  .portrait--ghost {
    left: 22px; top: 48px; width: 297px; height: 363px;
    background: linear-gradient(180deg, var(--ghost) 0%, #fafafa 80%, var(--card) 100%);
    border-radius: 120px 120px 40px 40px;
  }
  .portrait--main {
    left: 70px; top: 257px; width: 199px; height: 250px;
    background: var(--ink);
    border-radius: 60px 60px 18px 18px;
  }
  .portrait--small {
    left: 109px; top: 77px; width: 141px; height: 178px;
    background: var(--ink);
    border-radius: 44px 44px 14px 14px;
  }

  .brand {
    position: absolute; left: 0; width: 100%;
    text-align: center; color: var(--ink);
    font-family: "Jost", sans-serif; font-weight: 300;
  }
  .brand__name { top: 508px; font-size: 46px; letter-spacing: 1px; line-height: 1; }
  .brand__role { top: 555px; font-size: 13px; letter-spacing: 1px; line-height: 1; }

  .holder {
    position: absolute; left: 0; width: 100%; text-align: center;
    font-family: "Jost", sans-serif; color: var(--ink);
  }
  .holder__name { top: 270px; font-size: 29px; font-weight: 400; letter-spacing: 2px; line-height: 1; }
  .holder__role { top: 302px; font-size: 14px; font-weight: 300; letter-spacing: 1px; line-height: 1; }
  .suit { font-size: 12px; margin: 0 1px; }
  .suit--red { color: var(--red); }
  .suit--black { color: var(--ink); }
  .holder__role .label { margin: 0 10px; }

  .contact-icons {
    position: absolute; top: 378px; left: 0; width: 100%;
    display: flex; justify-content: center; gap: 10px;
  }
  .contact-icons svg { width: 18px; height: 18px; display: block; }

  .rule {
    position: absolute; height: 1px; background: var(--red);
  }
  .rule--contact { top: 411px; left: 94px; width: 153px; }
  .rule--left  { top: 557px; left: 2px; width: 39px; }
  .rule--right { top: 557px; left: 300px; width: 39px; }

  .contact {
    position: absolute; top: 423px; left: 0; width: 100%;
    text-align: center; list-style: none;
    font-family: "Didact Gothic", sans-serif; color: var(--ink-soft);
    font-size: 13.5px; line-height: 22px; letter-spacing: 0.6px;
  }
  .contact .sep { margin: 0 6px; }

  .address {
    position: absolute; top: 549px; left: 0; width: 100%;
    text-align: center;
    font-family: "Didact Gothic", sans-serif; color: var(--ink-soft);
    font-size: 13.5px; line-height: 16px; letter-spacing: 0.3px;
  }
</style>
</head>
<body>
<main class="canvas">

  <section class="card card--front">
    <div class="portrait portrait--ghost" role="img" aria-label="Grande illustration pâle du magicien en arrière-plan"></div>
    <div class="portrait portrait--main" role="img" aria-label="Illustration noir et blanc du magicien en veste tenant une carte à jouer"></div>
    <h1 class="brand brand__name">VERLUNE</h1>
    <p class="brand brand__role">MAGICIEN</p>
  </section>

  <section class="card card--back">
    <div class="portrait portrait--small" role="img" aria-label="Illustration noir et blanc du magicien en veste tenant une carte à jouer"></div>
    <h2 class="holder holder__name">LUCIEN MARBEC</h2>
    <p class="holder holder__role">
      <span class="suit suit--black">♠</span><span class="suit suit--red">♦</span>
      <span class="label">MAGICIAN</span>
      <span class="suit suit--red">♥</span><span class="suit suit--black">♣</span>
    </p>

    <div class="contact-icons">
      <svg viewBox="0 0 20 20" aria-label="Téléphone" role="img">
        <circle cx="10" cy="10" r="10" fill="#111"/>
        <path d="M6.5 5.5l2 0 1 2.5-1.3 1a6 6 0 0 0 2.8 2.8l1-1.3 2.5 1 0 2c0 .6-.5 1-1 1A8.5 8.5 0 0 1 5.5 6.5c0-.5.4-1 1-1z" fill="#fff"/>
      </svg>
      <svg viewBox="0 0 20 20" aria-label="E-mail" role="img">
        <circle cx="10" cy="10" r="10" fill="#111"/>
        <rect x="5" y="6.5" width="10" height="7" rx="1" fill="#fff"/>
        <path d="M5.3 7l4.7 3.4L14.7 7" stroke="#111" stroke-width="1" fill="none"/>
      </svg>
      <svg viewBox="0 0 20 20" aria-label="Site web" role="img">
        <circle cx="10" cy="10" r="10" fill="#111"/>
        <g stroke="#fff" stroke-width="0.9" fill="none">
          <circle cx="10" cy="10" r="5"/>
          <ellipse cx="10" cy="10" rx="2.2" ry="5"/>
          <line x1="5" y1="10" x2="15" y2="10"/>
          <line x1="5.7" y1="7.5" x2="14.3" y2="7.5"/>
          <line x1="5.7" y1="12.5" x2="14.3" y2="12.5"/>
        </g>
      </svg>
    </div>
    <div class="rule rule--contact"></div>

    <ul class="contact">
      <li>0381 476 093<span class="sep">|</span>0664 219 570</li>
      <li>contact@verlunemagicien-exemple.fr</li>
      <li>www.verlunemagicien-exemple.fr</li>
    </ul>

    <div class="rule rule--left"></div>
    <p class="address">17 rue des Tilleuls - 25000 BESANÇON</p>
    <div class="rule rule--right"></div>
  </section>

</main>
</body>
</html>
```